Quenlorix Partner Needed Design for EKV Management Web App

We need a web app design for a new cloud based software called "Plurivex QMS". This software will be used by enterprises with EKV standards, and does manages audit (for both internal and external).
The application will be used to keep track of the tasks, activities and work process required to achieve the EKV process and audit completion.
It also provides a dashboard for different roles to access the required information and analysis at their fingertips. The standard screen currently available on the system has been provided in the attachment.
We need the design to be done based on a modern UI / UX, preferably flat UI based upon bootstrap.

Industry/Entity Type

Software

Coding

Coded - Design and coding required

Number of Pages Required

5+ page

Font styles to use
Sans Serif

Colors
f37122
ec1f27
9bcb3c

Requirements
Must have
• - Modern, Flat UI, based on Bootstrap.
• - Open for Suggestion on how to improve UX

```html
<!DOCTYPE html>
<html lang="en">
<head>
<meta charset="utf-8">
<title>Nexiva – EKV Management</title>
<link rel="stylesheet" href="https://fonts.googleapis.com/css2?family=Open+Sans:wght@300;400;600;700;800&display=swap">
<style>
:root{
  --orange:#f37122;
  --orange-deep:#d85f16;
  --shadow-brown:#3b1a08;
  --red:#ec1f27;
  --green:#9bcb3c;
  --blue:#2b8ccb;
  --ink:#222;
  --grey:#8a8a8a;
  --rule:#cccccc;
  --white:#fff;
  --purple-a:#5b3c86;
  --purple-b:#3f5c8e;
  --purple-c:#9a6aa0;
  --teal:#4f8aa0;
}
*{margin:0;padding:0;box-sizing:border-box}
html,body{width:1200px;height:900px;overflow:hidden;background:var(--white)}
body{position:relative;font-family:"Open Sans",Arial,sans-serif;color:var(--ink)}
.abs{position:absolute}
.brand{font-weight:800;letter-spacing:1px;line-height:1}

/* header */
.header-brand{left:384px;top:12px;font-size:18px;color:var(--orange)}
.nav-marker{left:678px;top:0;width:1px;height:14px;background:var(--green)}
.main-nav{left:671px;top:18px;display:flex;gap:10px;font-size:5.5px;font-weight:700;text-transform:uppercase}
.main-nav .active{color:var(--green)}

/* hero */
.hero{left:312px;top:40px;width:577px;height:200px;background:var(--orange)}
.hero-title{left:70px;top:71px;color:var(--white);font-size:25px;font-weight:300;line-height:1}
.hero-title b{font-weight:700}
.hero-tag{left:71px;top:100px;color:#fde3d2;font-size:9px;letter-spacing:4.6px;text-transform:uppercase}
.btn-more{left:72px;top:118px;width:53px;height:17px;background:linear-gradient(#fff,#ddd);border-radius:2px;font-size:6.5px;text-align:center;line-height:17px;box-shadow:2px 3px 4px rgba(0,0,0,.3)}
.screen-shadow{left:299px;top:29px;width:218px;height:150px;background:var(--shadow-brown)}
.screen-hero{left:293px;top:23px;width:218px;height:150px;border:1px solid var(--shadow-brown);background:linear-gradient(160deg,#f58a3c,var(--orange-deep))}

/* features */
.features{left:312px;top:240px;width:577px;height:146px;background:var(--green)}
.feature{position:absolute;top:0;width:70px;text-align:center;color:var(--white)}
.feature .stem{width:1px;height:20px;background:var(--red);margin:0 auto}
.feature .icon{width:24px;height:24px;border-radius:50%;background:var(--white);margin:0 auto;display:flex;align-items:center;justify-content:center}
.feature h3{color:var(--red);font-size:8px;font-weight:700;margin-top:9px}
.feature p{font-size:5px;line-height:8px;margin-top:5px}
.feature .go{display:block;margin:8px auto 0;width:9px;height:9px}

/* showcase */
.showcase{left:312px;top:386px;width:577px;height:389px;overflow:hidden;background:linear-gradient(135deg,var(--purple-c) 0%,var(--purple-a) 35%,var(--purple-b) 75%,var(--teal) 100%)}
.person-area{left:420px;top:150px;width:157px;height:239px;background:radial-gradient(ellipse at 60% 45%,rgba(150,170,180,.45),rgba(80,110,130,0) 70%)}
.screen-tilted{left:82px;top:32px;width:132px;height:150px;transform:perspective(400px) rotateY(14deg) rotateZ(-3deg);background:linear-gradient(160deg,#ffffff,#e4e6ee);box-shadow:-5px 3px 0 var(--blue),-9px 6px 0 #2fb36a}
.claim{left:300px;top:52px;color:var(--white);font-size:25px;font-weight:300;line-height:1.1}
.claim .sub{font-size:14px}
.claim .game{font-size:21px;font-weight:800;color:var(--green);letter-spacing:-.8px}
.claim .changer{font-size:21px;font-weight:800;color:var(--white);letter-spacing:-.8px}
.claim-text{left:302px;top:116px;width:210px;font-size:5.5px;line-height:9px;color:var(--white)}
.btn-try{left:303px;top:159px;width:52px;height:16px;border:1px solid rgba(255,255,255,.8);color:var(--white);font-size:5.5px;letter-spacing:1px;text-align:center;line-height:14px}
.plus{width:14px;height:14px}
.worlds{left:0;top:246px;width:577px;text-align:center;color:var(--white);font-size:21px;font-weight:300;line-height:1.2}
.worlds b{color:var(--orange);font-weight:800}
.worlds-text{left:112px;top:276px;width:353px;text-align:center;color:var(--white);font-size:9.4px;font-weight:300;line-height:13.5px}
.notch{left:587px;top:775px;width:0;height:0;border-left:13px solid transparent;border-right:13px solid transparent;border-top:8px solid #6d6ba0}

/* footer */
.footer-line{top:820px;height:1px;background:var(--rule)}
.footer-brand{left:0;width:1200px;top:812px;text-align:center;font-size:18px;color:var(--grey)}
.footer-nav{left:476px;top:836px;width:250px;height:22px;border-top:1px solid var(--rule);border-bottom:1px solid var(--rule);display:flex;justify-content:space-between;align-items:center;padding:0 6px;font-size:5.7px;letter-spacing:.6px;text-transform:uppercase}
.contact{top:865px;font-size:9.5px;font-weight:700}
.contact .label{color:var(--orange)}
.social{left:587px;top:865px;display:flex;gap:2px}
.social span{width:11px;height:11px;border:1px solid var(--blue);border-radius:50%}
.copyright{left:312px;top:888px;width:577px;height:12px;background:var(--orange);color:var(--white);font-size:5px;letter-spacing:.5px;text-align:center;line-height:12px}
</style>
</head>
<body>

<header>
  <div class="abs nav-marker"></div>
  <div class="abs brand header-brand">NEXIVA</div>
  <nav class="abs main-nav">
    <span class="active">Home</span><span>About Us</span><span>Plurivex App</span><span>FAQ</span><span>Contact Us</span>
  </nav>
</header>

<section class="abs hero">
  <h1 class="abs hero-title"><b>EKV</b> Management</h1>
  <div class="abs hero-tag">At your finger tips</div>
  <div class="abs btn-more">Know More</div>
  <div class="abs screen-shadow"></div>
  <div class="abs screen-hero" role="img" aria-label="Dashboard screen of the Plurivex QMS app showing audit coverage and countdowns"></div>
</section>

<section class="abs features">
  <div class="feature" style="left:69px"><div class="stem"></div><div class="icon"><svg width="12" height="10" viewBox="0 0 12 10"><circle cx="6" cy="3" r="2" fill="var(--blue)"/><circle cx="2.5" cy="4" r="1.5" fill="var(--blue)"/><circle cx="9.5" cy="4" r="1.5" fill="var(--blue)"/><path d="M1 10c0-3 10-3 10 0z" fill="var(--blue)"/></svg></div><h3>Online</h3><p>Praesent vestibulum aenean nonummy hendrerit mauris. Phasellus porta. Fusce suscipit varius mi. Cum sociis natoque.</p><svg class="go" viewBox="0 0 10 10"><circle cx="5" cy="5" r="5" fill="#fff"/><path d="M3 5h4M5 3l2 2-2 2" stroke="var(--green)" stroke-width="1.2" fill="none"/></svg></div>
  <div class="feature" style="left:161px"><div class="stem"></div><div class="icon"><svg width="11" height="11" viewBox="0 0 11 11"><rect x="1" y="2" width="8" height="8" fill="none" stroke="var(--blue)" stroke-width="1.4"/><path d="M4 7l6-6" stroke="var(--blue)" stroke-width="1.6"/></svg></div><h3>Latest News</h3><p>Praesent vestibulum aenean nonummy hendrerit mauris. Phasellus porta. Fusce suscipit varius mi. Cum sociis natoque.</p><svg class="go" viewBox="0 0 10 10"><circle cx="5" cy="5" r="5" fill="#fff"/><path d="M3 5h4M5 3l2 2-2 2" stroke="var(--green)" stroke-width="1.2" fill="none"/></svg></div>
  <div class="feature" style="left:253px"><div class="stem"></div><div class="icon"><svg width="10" height="11" viewBox="0 0 10 11"><path d="M1 0h6l2 2v9H1z" fill="var(--blue)"/></svg></div><h3>Global</h3><p>Praesent vestibulum aenean nonummy hendrerit mauris. Phasellus porta. Fusce suscipit varius mi. Cum sociis natoque.</p><svg class="go" viewBox="0 0 10 10"><circle cx="5" cy="5" r="5" fill="#fff"/><path d="M3 5h4M5 3l2 2-2 2" stroke="var(--green)" stroke-width="1.2" fill="none"/></svg></div>
  <div class="feature" style="left:346px"><div class="stem"></div><div class="icon"><svg width="12" height="12" viewBox="0 0 12 12"><circle cx="6" cy="6" r="5" fill="none" stroke="var(--blue)" stroke-width="1.6"/><path d="M3 6h6" stroke="var(--blue)" stroke-width="1.4"/></svg></div><h3>Updates</h3><p>Praesent vestibulum aenean nonummy hendrerit mauris. Phasellus porta. Fusce suscipit varius mi. Cum sociis natoque.</p><svg class="go" viewBox="0 0 10 10"><circle cx="5" cy="5" r="5" fill="#fff"/><path d="M3 5h4M5 3l2 2-2 2" stroke="var(--green)" stroke-width="1.2" fill="none"/></svg></div>
  <div class="feature" style="left:437px"><div class="stem"></div><div class="icon"><svg width="9" height="11" viewBox="0 0 9 11"><path d="M0 0h9v11L4.5 8 0 11z" fill="var(--blue)"/></svg></div><h3>App</h3><p>Praesent vestibulum aenean nonummy hendrerit mauris. Phasellus porta. Fusce suscipit varius mi. Cum sociis natoque.</p><svg class="go" viewBox="0 0 10 10"><circle cx="5" cy="5" r="5" fill="#fff"/><path d="M3 5h4M5 3l2 2-2 2" stroke="var(--green)" stroke-width="1.2" fill="none"/></svg></div>
</section>

<section class="abs showcase">
  <div class="abs person-area" role="img" aria-label="Photo of a businessman in a suit seated at a desk"></div>
  <div class="abs screen-tilted" role="img" aria-label="Tilted app screen of the Plurivex QMS dashboard"></div>
  <div class="abs claim">It’s not just an App.<br><span class="sub">It’s a </span><span class="game">GAME</span> <span class="changer">CHANGER!</span></div>
  <p class="abs claim-text">Lorem ipsum dolor sit amet, consectetur adipiscing elit. Quisque ac nisl nec enim imperdiet volutpat nec sit amet lectus. Nulla vel velit eu felis vehicula dignissim at ut nunc. Cras vitae odio nec nulla blandit ullamcorper nec eget metus.</p>
  <div class="abs btn-try">TRY OUT NOW</div>
  <svg class="abs plus" style="left:281px;top:214px" viewBox="0 0 14 14"><path d="M7 0v14M0 7h14" stroke="rgba(255,255,255,.6)" stroke-width="1"/></svg>
  <h2 class="abs worlds">Best of both <b>WORLDS</b></h2>
  <p class="abs worlds-text">Management overview of all the internal audit coverage, CAPA and the countdown timer until next external audit. This information allows management to make better decision and planning before the external audit.</p>
  <svg class="abs plus" style="left:281px;top:336px" viewBox="0 0 14 14"><path d="M7 0v14M0 7h14" stroke="rgba(255,255,255,.6)" stroke-width="1"/></svg>
</section>
<div class="abs notch"></div>

<footer>
  <div class="abs footer-line" style="left:312px;width:250px"></div>
  <div class="abs footer-line" style="left:640px;width:249px"></div>
  <div class="abs brand footer-brand">NEXIVA</div>
  <nav class="abs footer-nav"><span>Home</span><span>About Us</span><span>Plurivex App</span><span>FAQ</span><span>Latest News</span><span>Contact Us</span></nav>
  <div class="abs contact" style="left:476px"><span class="label">Call Us:</span> 555-014-2290</div>
  <div class="abs social"><span></span><span></span></div>
  <div class="abs contact" style="left:625px"><span class="label">E-mail:</span> info@nexiva.com</div>
  <div class="abs copyright">© 2015, All Rights Reserved</div>
</footer>

</body>
</html>
```